Travel Group 'Lydgate Group' needs a new business card design

Lydgate Group is a diverse business specialising in bespoke, tailor made holidays to suit all budgets and we are specialists in planning exciting day/short trips to suit all markets. Our target market is very varied going from the corporate client and as well as people in the community who simply want to experience something special.
We are looking for a card design that will encourage people to look at our websites and social media platforms and to see for themselves the different facets to our business. It is essential that the card has social media icons for Facebook, Twitter and Instagram. We are looking for a card with a blank background with no pictures and for the front side to have the attached Lydgate logo. The card should have similar colour scheme to the attached Lydgate logo.
The card must have the following information on one side:
Maud Penrose
Business Development Manager
maudpenrose@lydgatevoyages.example
Lydgate Group, 87 Quarry Lane
Brackenmoor, Westmarch, Scotland KA19 4TN
+44 (0)1632 730182
And then the card must have the following on the second side:
(Lydgate logo)
(social media icons)
www.lydgatevoyages.example
www.lydgateoutings.example
Target Market(s)
Our target market is very varied going from the corporate client and as well as people in the community who simply want to experience something special.
Industry/Entity Type
Business
Contact Information for Business Card
Maud Penrose
+44 (0)1632 730182
(Lydgate logo)
(social media icons)
www.lydgatevoyages.example
www.lydgateoutings.example
Requirements
Must have
- It is essential that the card has social media icons for Facebook, Twitter & Instagram.
Should not have
- Should not have any images other than Lydgate logo.

```html
<!DOCTYPE html>
<html lang="en">
<head>
<meta charset="utf-8">
<title>Lydgate Group – Business Card</title>
<link rel="stylesheet" href="https://fonts.googleapis.com/css2?family=Open+Sans:wght@400;700&display=swap">
<style>
  :root {
    --backdrop: #ebebeb;
    --card: #ffffff;
    --purple: #5a3a98;
    --ink: #47307f;
    --navy: #2a2462;
    --pink: #e0258f;
    --shadow: rgba(0,0,0,0.18);
  }
  * { margin: 0; padding: 0; box-sizing: border-box; }
  html, body { width: 1200px; height: 900px; overflow: hidden; background: var(--backdrop); }
  body { font-family: "Open Sans", Verdana, sans-serif; position: relative; }

  .card {
    position: absolute;
    top: 100px;
    width: 420px;
    height: 680px;
    background: var(--card);
    border-radius: 20px;
    box-shadow: 0 4px 14px var(--shadow);
    overflow: hidden;
  }
  .card--contact { left: 150px; }
  .card--brand { left: 630px; }

  /* Contact side */
  .holder { position: absolute; left: 40px; top: 44px; }
  .holder__name { font-size: 34px; font-weight: 700; color: var(--purple); letter-spacing: 1px; line-height: 1.1; }
  .holder__role { font-size: 17px; color: var(--pink); margin-top: 4px; }

  .details { position: absolute; left: 40px; right: 24px; top: 146px; list-style: none; }
  .details__group { margin-bottom: 16px; }
  .details__row { display: flex; align-items: flex-start; gap: 12px; font-size: 16px; color: var(--ink); line-height: 1.5; white-space: nowrap; }
  .details__icon { width: 16px; height: 16px; flex: none; margin-top: 4px; fill: var(--pink); }
  .details__dot { width: 12px; height: 12px; flex: none; margin: 6px 2px 0; border-radius: 50%; background: var(--pink); }

  .wordmark { position: absolute; display: flex; align-items: center; gap: 12px; color: var(--navy); font-weight: 700; letter-spacing: 6px; }
  .wordmark__mark { border-radius: 50%; background: var(--pink); flex: none; }
  .card--contact .wordmark { left: 40px; bottom: 64px; font-size: 42px; }
  .card--contact .wordmark__mark { width: 22px; height: 22px; }

  /* Brand side */
  .card--brand .wordmark { left: 50%; top: 290px; transform: translateX(-50%); font-size: 50px; }
  .card--brand .wordmark__mark { width: 26px; height: 26px; }

  .socials { position: absolute; left: 0; right: 0; bottom: 58px; display: flex; justify-content: center; align-items: center; gap: 14px; }
  .socials__rule { width: 50px; height: 2px; background: var(--pink); }
  .socials__icon { width: 30px; height: 30px; border-radius: 50%; background: var(--purple); }
</style>
</head>
<body>

<section class="card card--contact" aria-label="Contact side">
  <header class="holder">
    <h1 class="holder__name">Maud Penrose</h1>
    <p class="holder__role">Business Development Manager</p>
  </header>

  <ul class="details">
    <li class="details__group">
      <div class="details__row">
        <svg class="details__icon" viewBox="0 0 16 16" aria-hidden="true"><circle cx="8" cy="8" r="7" fill="none" stroke="var(--pink)" stroke-width="1.6"/><path d="M5.2 4.5l1.4-.3.8 1.9-.9.7c.4.9 1.1 1.6 2 2l.7-.9 1.9.8-.3 1.4c-3 .2-5.8-2.6-5.6-5.6z"/></svg>
        <span>+44 (0)1632 730182</span>
      </div>
      <div class="details__row">
        <svg class="details__icon" viewBox="0 0 16 16" aria-hidden="true"><rect x="1" y="3" width="14" height="10" rx="1"/><path d="M1.5 3.8L8 9l6.5-5.2" fill="none" stroke="#fff" stroke-width="1.3"/></svg>
        <span>maudpenrose@lydgatevoyages.example</span>
      </div>
    </li>
    <li class="details__group">
      <div class="details__row">
        <svg class="details__icon" viewBox="0 0 16 16" aria-hidden="true"><circle cx="8" cy="8" r="7"/><path d="M1 8h14M8 1c-3 3.5-3 10.5 0 14M8 1c3 3.5 3 10.5 0 14" fill="none" stroke="#fff" stroke-width="1.1"/></svg>
        <span>www.lydgatevoyages.example</span>
      </div>
      <div class="details__row">
        <svg class="details__icon" viewBox="0 0 16 16" aria-hidden="true"><circle cx="8" cy="8" r="7"/><path d="M1 8h14M8 1c-3 3.5-3 10.5 0 14M8 1c3 3.5 3 10.5 0 14" fill="none" stroke="#fff" stroke-width="1.1"/></svg>
        <span>www.lydgateoutings.example</span>
      </div>
    </li>
    <li class="details__group">
      <div class="details__row">
        <svg class="details__icon" viewBox="0 0 16 16" aria-hidden="true"><path d="M8 1a5 5 0 0 0-5 5c0 4 5 9 5 9s5-5 5-9a5 5 0 0 0-5-5z"/><circle cx="8" cy="6" r="2" fill="#fff"/></svg>
        <span>Lydgate Group, 87 Quarry Lane<br>Brackenmoor, Westmarch, Scotland KA19 4TN</span>
      </div>
    </li>
    <li class="details__group">
      <div class="details__row"><i class="details__dot"></i><span>www.chirper.example/lydgatevoyages</span></div>
      <div class="details__row"><i class="details__dot"></i><span>www.friendbook.example/lydgateoutings</span></div>
      <div class="details__row"><i class="details__dot"></i><span>www.snapgram.example/lydgatevoyages</span></div>
    </li>
  </ul>

  <div class="wordmark"><span class="wordmark__mark"></span><span>LYDGATE</span></div>
</section>

<section class="card card--brand" aria-label="Brand side">
  <div class="wordmark"><span class="wordmark__mark"></span><span>LYDGATE</span></div>

  <nav class="socials" aria-label="Social media">
    <span class="socials__rule"></span>
    <span class="socials__icon" role="img" aria-label="Friendbook"></span>
    <span class="socials__icon" role="img" aria-label="Chirper"></span>
    <span class="socials__icon" role="img" aria-label="Snapgram"></span>
    <span class="socials__rule"></span>
  </nav>
</section>

</body>
</html>
```